Stationary for New Company

We need stationary designed for a new company. Details of the required stationary is attached.

The final version should be trendy, clean... only 2 colours (green + grey/black) and professional.

#1: Business Cards (design on 2 sides)
#2: Letterhead (word format)
#3: Cover Page and back cover for proposals
#4: Envelopes,
#5: Thank You card,
#6: Presentation Folder,
#7: Email signatures template (sample attached in word document)

Logo is attached. Logo can be reversed out (will attach once available). Logo can be stacked or horizontal (provided as horizontal).

Files need to be provided in ai + png format.

Target Market(s)

Business owners. More affluent.

Industry/Entity Type

Business

Requirements
Must have
• See brief

Font: Calibri
Should not have
• Photographs / stock photos

```html
<!DOCTYPE html>
<html lang="en">
<head>
<meta charset="utf-8">
<title>Crestway Insurance Brokers – Stationery Suite</title>
<link href="https://fonts.googleapis.com/css2?family=Carlito:wght@400&display=swap" rel="stylesheet">
<style>
  :root {
    --backdrop: #8aaa6c;
    --paper: #f1f1f1;
    --ink-dark: #2b2a2c;
    --brand-green: #4f8a2e;
    --text-grey: #8a8a8a;
    --fold-line: #d9d9d9;
  }
  html, body {
    margin: 0;
    padding: 0;
    width: 1200px;
    height: 1000px;
    overflow: hidden;
    background: var(--backdrop);
  }
  .suite { display: block; width: 1200px; height: 1000px; }
  .suite text { font-family: "Carlito", sans-serif; }
  .paper { fill: var(--paper); }
  .dark { fill: var(--ink-dark); }
  .brand-square { fill: var(--brand-green); }
  .brand-name { fill: var(--brand-green); font-weight: 400; }
  .contact-line { fill: var(--text-grey); font-size: 3.6px; }
  .card-text { fill: var(--text-grey); font-size: 3.4px; }
  .card-name { fill: #555; font-size: 4.6px; }
  .fold { stroke: var(--fold-line); stroke-width: 1; }
</style>
</head>
<body>
<svg class="suite" viewBox="0 0 1200 1000" xmlns="http://www.w3.org/2000/svg">

  <!-- Letterhead -->
  <g class="letterhead">
    <rect class="paper" x="174" y="110" width="259" height="367"/>
    <rect class="brand-square" x="195" y="130" width="20" height="20"/>
    <text class="brand-name" x="219" y="143" font-size="15">Crestway</text>
    <text class="brand-name" x="219" y="151" font-size="6.5">Insurance Brokers</text>
    <text class="contact-line" x="195" y="457">Address: 18 Market Lane, Suite 4, Fairview, NL 40218</text>
    <text class="contact-line" x="195" y="463">Phone: 555 0142 | Fax: 555 0143 | Toll free: 555 0100</text>
    <text class="contact-line" x="195" y="469">Email: info@crestway.example | www.crestway.example</text>
  </g>

  <!-- Envelope, open flap -->
  <g class="envelope envelope--open">
    <path class="dark" d="M474,240 L480,166 Q481,158 489,158 L730,158 Q738,158 739,166 L745,240 Z"/>
    <rect class="paper" x="474" y="238" width="271" height="107"/>
    <rect class="brand-square" x="699" y="174" width="16" height="16"/>
  </g>

  <!-- Envelope, front -->
  <g class="envelope envelope--front">
    <rect class="paper" x="778" y="158" width="272" height="138"/>
    <rect class="brand-square" x="790" y="170" width="17" height="17"/>
    <text class="brand-name" x="811" y="181" font-size="12.5">Crestway</text>
    <text class="brand-name" x="811" y="188" font-size="5.5">Insurance Brokers</text>
    <text class="contact-line" x="790" y="279">Address: 18 Market Lane, Suite 4, Fairview, NL 40218</text>
    <text class="contact-line" x="790" y="284">Phone: 555 0142 | Fax: 555 0143 | Toll free: 555 0100</text>
    <text class="contact-line" x="790" y="289">Email: info@crestway.example | www.crestway.example</text>
  </g>

  <!-- Envelope, back -->
  <g class="envelope envelope--back">
    <rect class="paper" x="778" y="336" width="272" height="136"/>
    <path class="dark" d="M778,336 L1050,336 L1046,383 Q1044,390 1036,390 L792,390 Q784,390 782,383 Z"/>
    <rect class="brand-square" x="910" y="350" width="10" height="10"/>
    <text class="brand-name" x="915" y="369" font-size="8" text-anchor="middle">Crestway</text>
  </g>

  <!-- Business card, front -->
  <g class="business-card business-card--front">
    <rect class="dark" x="478" y="406" width="106" height="69"/>
    <rect class="brand-square" x="524" y="424" width="11" height="11"/>
    <text class="brand-name" x="531" y="449" font-size="10" text-anchor="middle">Crestway</text>
    <text class="brand-name" x="531" y="455" font-size="4.5" text-anchor="middle">Insurance Brokers</text>
  </g>

  <!-- Business card, back -->
  <g class="business-card business-card--back">
    <rect class="paper" x="627" y="406" width="106" height="69"/>
    <path class="dark" d="M627,438 Q655,436 675,452 Q695,468 733,468 L733,475 L627,475 Z"/>
    <rect class="brand-square" x="709" y="412" width="8" height="8"/>
    <text class="brand-name" x="713" y="427" font-size="5.5" text-anchor="middle">Crestway</text>
    <text class="card-name" x="633" y="423">Jordan Hale, BA, CFIS</text>
    <text class="card-text" x="633" y="428">Insurance Broker</text>
    <text class="card-text" x="633" y="434">Phone: 555 0142</text>
    <text class="card-text" x="633" y="438">Mobile: 555 0177</text>
    <text class="card-text" x="633" y="442">Email: jordan@crestway.example</text>
    <text class="card-text" x="633" y="446">Web: www.crestway.example</text>
  </g>

  <!-- Proposal cover -->
  <g class="proposal-cover">
    <rect class="dark" x="152" y="515" width="283" height="383"/>
    <path class="paper" d="M152,515 L435,515 L435,668 Q420,624 330,618 Q232,611 192,572 Q166,545 152,522 Z"/>
    <rect class="brand-square" x="362" y="537" width="26" height="26"/>
    <text class="brand-name" x="414" y="585" font-size="21" text-anchor="end">Crestway</text>
    <text class="brand-name" x="414" y="595" font-size="9" text-anchor="end">Insurance Brokers</text>
  </g>

  <!-- Presentation folder, open -->
  <g class="presentation-folder">
    <rect class="paper" x="478" y="512" width="568" height="380"/>
    <line class="fold" x1="762" y1="512" x2="762" y2="892"/>
    <path class="dark" d="M478,892 L478,770 L745,770 Q757,770 757,782 L757,892 Z"/>
    <path class="dark" d="M767,892 L767,782 Q767,770 779,770 L1046,770 L1046,892 Z"/>
    <rect class="brand-square" x="1016" y="781" width="9" height="9"/>
    <text class="brand-name" x="1020" y="800" font-size="7" text-anchor="middle">Crestway</text>
  </g>

</svg>
</body>
</html>
```